Restaurant Posters

Looking for two posters to be created for restaurant promos - see below for details:

Design #1 -
Want to highlight two main specials we offer - first is Tuesday BOGO Burgers (with purchase of two beverages), second is on Wednesday's we offer $0.75 Wings (includes traditional and boneless) and $2 off IPA's

Then at the bottom smaller would like to call out two less important offers - first is $2 off Nebraska Beers on Mondays, and the second is 1/2 off 19.2oz Crowlers on Thursdays

Design #2 -
Looking to create a sign up for our e-club and receive a free appetizer upon sign up, free burger on your birthday week, and access to exclusive deals and email offers

See attached for supporting docs you may use - don't have to but feel free to get creative with these. Would like the designs to be simple, and follow our brand look and feel as much as possible. Our website is not a good indication of our brand - I would go more off of our logos, and our menu design.

Need extra days to review

```html
<!DOCTYPE html>
<html lang="en">
<head>
<meta charset="utf-8">
<title>Daily Specials Poster</title>
<link rel="stylesheet" href="https://fonts.googleapis.com/css2?family=Oswald:wght@500;600;700&family=Montserrat:wght@800&family=Bitter:wght@400&display=swap">
<style>
  :root {
    --red: #c8102e;
    --red-light: #dc2d48;
    --red-text: #c8102e;
    --white: #ffffff;
    --page: #f1f1f1;
    --img-warm: #d9a05a;
    --img-silver: #c9cacc;
    --img-gold: #e8b43a;
  }
  * { box-sizing: border-box; margin: 0; padding: 0; }
  html, body { width: 1200px; height: 1200px; overflow: hidden; background: var(--page); }
  .poster {
    position: absolute; left: 176px; top: 0;
    width: 848px; height: 1200px; background: var(--white);
  }
  .poster-title {
    position: absolute; left: 45px; top: 38px;
    font: 700 50px/1 "Oswald", sans-serif; color: var(--red-text);
    letter-spacing: 0.5px;
  }
  .panel {
    position: absolute; color: var(--white);
    background: linear-gradient(90deg, var(--red) 0%, var(--red-light) 55%, var(--red) 100%);
  }
  .panel--tuesday { left: 45px; top: 113px; width: 761px; height: 270px; }
  .panel--wednesday { left: 45px; top: 474px; width: 761px; height: 223px; }
  .panel--monday { left: 45px; top: 812px; width: 351px; height: 253px; }
  .panel--thursday { left: 460px; top: 812px; width: 346px; height: 253px; }
  .day {
    position: absolute; left: 25px; top: 26px;
    font: 600 38px/1 "Oswald", sans-serif; letter-spacing: 0.5px;
  }
  .small .day { font-size: 34px; }
  .offer {
    position: absolute; left: 25px;
    font: 800 24px/1.12 "Montserrat", sans-serif; letter-spacing: 4px; text-transform: uppercase;
  }
  .offer--big { font-size: 44px; letter-spacing: 6px; line-height: 1.14; }
  .offer--mid { font-size: 28px; letter-spacing: 3.5px; }
  .offer--side { left: 488px; top: 80px; }
  .note {
    position: absolute; left: 25px;
    font: 400 18px/1.25 "Bitter", serif;
  }
  .note--small { font-size: 16px; }
  .timings {
    position: absolute; left: 25px;
    font: 500 16px/1 "Oswald", sans-serif;
  }
  .timings b { font-weight: 700; font-size: 17px; margin-left: 6px; }
  .photo { position: absolute; border-radius: 18px; }
  .photo--burger {
    left: 397px; top: 144px; width: 409px; height: 289px;
    background: linear-gradient(90deg, var(--img-warm) 0%, #b8743a 50%, var(--img-silver) 60%, #e4e5e7 100%);
  }
  .photo--wings {
    left: 330px; top: 513px; width: 180px; height: 246px;
    background: linear-gradient(180deg, #f3f1e6 0%, var(--img-gold) 35%, #c0672a 100%);
  }
  .photo--pint {
    left: 261px; top: 887px; width: 128px; height: 219px;
    background: linear-gradient(180deg, #fbfbfb 0%, var(--img-gold) 40%, #f0c860 100%);
  }
  .photo--can {
    left: 672px; top: 880px; width: 128px; height: 240px;
    background: linear-gradient(180deg, var(--img-gold) 0%, #f0c860 22%, var(--img-silver) 38%, #9fa1a4 100%);
  }
  .divider { position: absolute; stroke: var(--red); stroke-width: 1.5; stroke-dasharray: 5 4; }
</style>
</head>
<body>
<main class="poster">
  <h1 class="poster-title">DAILY SPECIALS</h1>

  <section class="panel panel--tuesday">
    <h2 class="day">TUESDAYS:</h2>
    <p class="offer offer--big" style="top:82px">BOGO<br>BURGERS</p>
    <p class="note" style="top:194px">With purchase of 2 beverages.</p>
    <p class="timings" style="top:228px">Timings: <b>4pm onwards</b></p>
  </section>
  <div class="photo photo--burger" role="img" aria-label="Photo of a loaded burger beside two silver beer cans"></div>

  <svg class="divider" width="848" height="1200" style="left:0;top:0" aria-hidden="true">
    <line x1="45" y1="451" x2="806" y2="451"/>
    <line x1="45" y1="788" x2="806" y2="788"/>
    <line x1="425" y1="804" x2="425" y2="1160"/>
    <line x1="45" y1="1154" x2="806" y2="1154"/>
  </svg>

  <section class="panel panel--wednesday">
    <h2 class="day">WEDNESDAYS:</h2>
    <p class="offer offer--mid" style="top:80px">$0.75 WINGS</p>
    <p class="note note--small" style="top:124px">Your choice of Bone-in<br>or Boneless wings.</p>
    <p class="timings" style="top:184px">Timings: <b>All Day</b></p>
    <p class="offer offer--mid offer--side">AND $2 OFF<br>IPA PINTS</p>
  </section>
  <div class="photo photo--wings" role="img" aria-label="Photo of a pint of beer with golden fried bites"></div>

  <section class="panel panel--monday small">
    <h2 class="day">MONDAYS:</h2>
    <p class="offer" style="top:74px">$2 OFF<br>NEBRASKA<br>BREWED<br>BEERS<br>ON TAP</p>
    <p class="timings" style="top:222px">Timings: <b>All Day</b></p>
  </section>
  <div class="photo photo--pint" role="img" aria-label="Photo of a pint glass of lager splashing"></div>

  <section class="panel panel--thursday small">
    <h2 class="day" style="left:20px">THURSDAYS:</h2>
    <p class="offer" style="left:22px;top:90px">½ OFF<br>19.2 OZ<br>CROWLERS</p>
    <p class="timings" style="left:22px;top:222px">Timings: <b>All Day</b></p>
  </section>
  <div class="photo photo--can" role="img" aria-label="Photo of a silver crowler can with beer splashing out"></div>
</main>
</body>
</html>
```